Criação de Papelaria (6 itens) para Beleza
" REALIZANDO CIRURGIAS PLÁSTICAS EM PACIENTES QUE DESEJAM MELHORIAS NO CONTORNO CORPORAL OU EM ALGO QUE OS INCOMODE EM SUA APARÊNCIA "

```html
<!DOCTYPE html>
<html lang="pt-BR">
<head>
<meta charset="utf-8">
<title>Lucas Verano – Pasta</title>
<link rel="stylesheet" href="https://fonts.googleapis.com/css2?family=Michroma&family=Open+Sans:wght@400;600&display=swap">
<style>
  :root{
    --bg:#e4e4e4;
    --band:#ffffff;
    --paper:#ffffff;
    --ink:#3a3a3a;
    --ink-soft:#8a8a8a;
    --icon:#6b6b6b;
    --fold:#d6d6d6;
    --ghost:#f3f3f3;
  }
  *{margin:0;padding:0;box-sizing:border-box}
  html,body{width:1200px;height:1200px;overflow:hidden;background:var(--bg)}
  body{position:relative;font-family:"Open Sans",sans-serif;color:var(--ink)}

  .contact-band{position:absolute;left:0;top:0;width:1200px;height:192px;background:var(--band)}
  .contact{display:flex;align-items:center;gap:12px;line-height:1.1;white-space:nowrap}
  .contact-band .contact{position:absolute;top:86px;height:56px;font-size:24px}
  .contact-band .contact svg{width:42px;height:42px;flex:none}
  .contact--phone{left:72px}
  .contact--address{left:346px}
  .contact--email{left:626px}
  .contact--social{left:972px}

  .folder{position:absolute;left:44px;top:209px;width:1108px;height:782px;display:flex;
    box-shadow:0 6px 18px rgba(0,0,0,.12)}
  .panel{position:relative;flex:1;background:var(--paper);overflow:hidden}
  .panel--back{border-right:2px solid var(--fold)}

  .ghost-circle{position:absolute;border-radius:50%;background:var(--ghost)}
  .panel--back .ghost-circle{width:520px;height:520px;right:-300px;top:110px}
  .panel--front .ghost-circle{width:520px;height:520px;left:-220px;top:110px}

  .brand{display:flex;align-items:center;gap:10px;position:absolute}
  .brand__dot{border-radius:50%;background:var(--ink-soft);flex:none}
  .brand__name{font-family:"Michroma",sans-serif;color:var(--ink-soft);letter-spacing:.02em;white-space:nowrap}
  .brand__sub{font-family:"Michroma",sans-serif;color:var(--ink-soft);letter-spacing:.42em;white-space:nowrap}

  .panel--back .brand{left:196px;top:95px}
  .panel--back .brand__dot{width:10px;height:10px}
  .panel--back .brand__name{font-size:11px}

  .panel--front .brand{left:132px;top:382px;align-items:flex-start;gap:12px}
  .panel--front .brand__dot{width:24px;height:24px;margin-top:4px}
  .panel--front .brand__name{font-size:24px;line-height:1.2}
  .panel--front .brand__sub{font-size:10px;margin-top:6px}

  .panel-contacts{position:absolute;left:62px;bottom:26px;display:flex;gap:20px;align-items:center}
  .panel-contacts .contact{font-size:9px;gap:5px;color:var(--ink-soft)}
  .panel-contacts .contact svg{width:15px;height:15px}
</style>
</head>
<body>
  <header class="contact-band">
    <div class="contact contact--phone">
      <svg viewBox="0 0 44 44"><circle cx="22" cy="22" r="21" fill="var(--icon)"/><path d="M15 12c2-1 3 0 4 3s0 3-1 4c1 3 3 5 6 6 1-1 2-2 4-1s4 2 3 4-3 3-5 3C17 30 12 22 14 14z" fill="#fff"/></svg>
      <span>(xx) xxxx-xxxx<br>(xx) xxxx-xxxx</span>
    </div>
    <div class="contact contact--address">
      <svg viewBox="0 0 44 44"><circle cx="22" cy="22" r="21" fill="var(--icon)"/><path d="M22 10a8 8 0 0 0-8 8c0 6 8 15 8 15s8-9 8-15a8 8 0 0 0-8-8zm0 11a3 3 0 1 1 0-6 3 3 0 0 1 0 6z" fill="#fff"/></svg>
      <span>R. Seu Endereço<br>Cidade - Bairro</span>
    </div>
    <div class="contact contact--email">
      <svg viewBox="0 0 44 44"><circle cx="22" cy="22" r="21" fill="var(--icon)"/><rect x="11" y="14" width="22" height="16" rx="2" fill="#fff"/><path d="M11 15l11 8 11-8" stroke="var(--icon)" stroke-width="2" fill="none"/></svg>
      <span>seuemail@exemplo.com</span>
    </div>
    <div class="contact contact--social">
      <svg viewBox="0 0 44 44"><circle cx="22" cy="22" r="21" fill="var(--icon)"/></svg>
      <span>Rede Social</span>
    </div>
  </header>

  <main class="folder">
    <section class="panel panel--back">
      <div class="ghost-circle"></div>
      <div class="brand">
        <span class="brand__dot"></span>
        <span class="brand__name">LUCAS VERANO</span>
      </div>
      <div class="panel-contacts">
        <div class="contact">
          <svg viewBox="0 0 44 44"><circle cx="22" cy="22" r="21" fill="var(--icon)"/><path d="M15 12c2-1 3 0 4 3s0 3-1 4c1 3 3 5 6 6 1-1 2-2 4-1s4 2 3 4-3 3-5 3C17 30 12 22 14 14z" fill="#fff"/></svg>
          <span>(xx) xxxx-xxxx<br>(xx) xxxx-xxxx</span>
        </div>
        <div class="contact">
          <svg viewBox="0 0 44 44"><circle cx="22" cy="22" r="21" fill="var(--icon)"/><path d="M22 10a8 8 0 0 0-8 8c0 6 8 15 8 15s8-9 8-15a8 8 0 0 0-8-8zm0 11a3 3 0 1 1 0-6 3 3 0 0 1 0 6z" fill="#fff"/></svg>
          <span>R. Seu Endereço<br>Cidade - Bairro</span>
        </div>
        <div class="contact">
          <svg viewBox="0 0 44 44"><circle cx="22" cy="22" r="21" fill="var(--icon)"/><rect x="11" y="14" width="22" height="16" rx="2" fill="#fff"/></svg>
          <span>seuemail@exemplo.com</span>
        </div>
        <div class="contact">
          <svg viewBox="0 0 44 44"><circle cx="22" cy="22" r="21" fill="var(--icon)"/></svg>
          <span>Rede Social</span>
        </div>
      </div>
    </section>

    <section class="panel panel--front">
      <div class="ghost-circle"></div>
      <div class="brand">
        <span class="brand__dot"></span>
        <div>
          <div class="brand__name">LUCAS VERANO</div>
          <div class="brand__sub">CIRURGIA PLÁSTICA</div>
        </div>
      </div>
    </section>
  </main>
</body>
</html>
```